Dermatology Clinic / Pediatric Clinic / Allergy Clinic

Its a school project so just make up all the information on the flyer.
i need "3 DIFFERENT FLYERS. All 8x12. Can be edited through Microsoft word.
DUE DATE: FRIDAY JUNE 10, 2016 NOT JUNE 22, 2016
First Name of the Project is: Dermatology Clinic,
Second Name of the Project is: Pediatric Clinic,
Last Name of the Project is: Allergy Clinic.
My professors instruction: A prospective client should be able to see your ad and know everything about the specialist and why they might need one. Be sure to utilize colors and pictures.
has accurate information on each flyers. Good knowledge of subject and presentation package well done.
flyer to advertise and promote service AND INFORMATION ON MY CHOSEN PROJECTS to help people gain more knowledge on each specialties.
ON THE FLYERS IT INCLUDE:
1) What services are offered
2) specialties of the clinic
3) Name of the doctor: Corinne Mae Delacruz
4) Address: Address: 415 Birchmere Rd. E. Suite 210, Toronto, ON M4K 2P7
5) Phone:(416) 555-0187
6) Clinic Hours:
(By appointment only)
Monday to Thursday: 8:30am – 3:30pm
Friday: 9:00am – 3:30pm
Saturday & Sunday: Close
and any other necessary information.
Updates
Target Market(s)
Deadline is on July 10, 2016
I dunno how to update the date. :( but it will be soon. July 10 Friday
Visual reminder for professionals working who can generate referrals. Friends and family who would like to purchase a gift certificate for friend/family member.
Pls help. Thank you
Industry/Entity Type
School
Requirements
Must have
- On the flyer it includes.
- 1) What services are offered
- 2) specialties of the clinic
- 3) Name of the doctor: Corinne Mae Delacruz
- 4) Address: Address: 415 Birchmere Rd. E. Suite 210, Toronto, ON M4K 2P7
- 5) Phone:(416) 555-0187
- and any other necessary information.
Nice to have
- made and can open and edit on Microsoft Word

```html
<!DOCTYPE html>
<html lang="en">
<head>
<meta charset="utf-8">
<title>Clearleaf Clinic – Dermatology Flyer</title>
<link href="https://fonts.googleapis.com/css2?family=PT+Sans:ital,wght@0,400;1,400&family=PT+Sans+Narrow:wght@700&family=Open+Sans:wght@300;400&display=swap" rel="stylesheet">
<style>
  :root {
    --stage: #ebe8e4;
    --paper: #ffffff;
    --leaf-green: #8cc63f;
    --slate: #4a5d66;
    --ink: #1c1c1c;
    --teal-grey: #3f5a66;
    --hair-gold: #d8b784;
    --hair-light: #efdcbc;
    --skin: #f1d3c2;
    --skin-light: #f8e8de;
  }
  * { box-sizing: border-box; margin: 0; padding: 0; }
  html, body {
    width: 1200px; height: 1200px; overflow: hidden;
    background: var(--stage);
  }
  .flyer {
    position: absolute; left: 30px; top: 220px;
    width: 1140px; height: 760px;
    background: var(--paper);
    box-shadow: 0 10px 30px rgba(0,0,0,0.18);
    overflow: hidden;
  }
  .hero-photo {
    position: absolute; left: 0; top: 0; width: 1140px; height: 503px;
    background:
      radial-gradient(ellipse 420px 300px at 820px 280px, var(--skin-light) 0%, var(--skin) 45%, rgba(241,211,194,0) 100%),
      linear-gradient(90deg, var(--hair-gold) 0%, var(--hair-light) 40%, #e9c8a8 60%, var(--skin) 80%, #ffffff 100%);
  }
  .lower-backdrop {
    position: absolute; left: 0; top: 503px; width: 594px; height: 257px;
    background: linear-gradient(180deg, #f3ece2 0%, #fbf8f4 45%, #ffffff 100%);
  }
  .brand-box {
    position: absolute; left: 58px; top: 0; width: 257px; height: 260px;
    background: rgba(255,255,255,0.88);
    display: flex; flex-direction: column; align-items: center; justify-content: flex-end;
    padding-bottom: 20px;
    font-family: "PT Sans", sans-serif;
  }
  .brand-name {
    display: flex; align-items: center; gap: 9px;
    font-size: 24px; font-weight: 400; color: var(--leaf-green);
    letter-spacing: 0.5px; margin-bottom: 14px;
  }
  .brand-dot {
    width: 16px; height: 16px; border-radius: 50%; background: var(--leaf-green);
  }
  .brand-address {
    font-size: 18px; line-height: 25px; color: #333; text-align: center;
  }
  .headline {
    position: absolute; left: 58px; top: 282px;
    font-family: "PT Sans Narrow", sans-serif; font-weight: 700;
    font-size: 60px; line-height: 64px; color: #ffffff;
    text-transform: uppercase; letter-spacing: 0.5px;
    text-shadow: 2px 3px 5px rgba(0,0,0,0.45);
  }
  .doctor-info {
    position: absolute; left: 58px; top: 527px;
    font-family: "PT Sans", sans-serif; color: #333;
  }
  .doctor-name { font-size: 29px; color: var(--ink); margin-bottom: 10px; }
  .hours-title { font-size: 21px; color: var(--teal-grey); line-height: 29px; }
  .hours-note { font-size: 21px; font-style: italic; color: var(--ink); line-height: 29px; }
  .hours-line { font-size: 21px; line-height: 29px; color: #333; }
  .services-panel {
    position: absolute; left: 594px; top: 503px; width: 546px; height: 174px;
    background: var(--leaf-green);
    padding: 34px 40px 0 57px;
    font-family: "Open Sans", sans-serif; font-weight: 300;
    font-size: 25px; line-height: 33px; color: #ffffff;
  }
  .footer-band {
    position: absolute; left: 594px; top: 677px; width: 546px; height: 83px;
    background: var(--slate);
  }
</style>
</head>
<body>
  <main class="flyer">
    <div class="hero-photo" role="img" aria-label="Photo of a woman with long blonde hair resting with eyes closed, hand on her cheek, a white lily by her chin"></div>
    <div class="lower-backdrop" role="img" aria-label="Soft, faded blonde hair background"></div>

    <header class="brand-box">
      <div class="brand-name"><span class="brand-dot"></span>Clearleaf Clinic</div>
      <p class="brand-address">415 Birchmere Rd. E. Suite<br>210, Toronto, ON M4K 2P7</p>
    </header>

    <h1 class="headline">Rejuvenate,<br>Revitalize and<br>Renew your skin</h1>

    <section class="doctor-info">
      <h2 class="doctor-name">Corinne Mae Delacruz, MD FAAD</h2>
      <p class="hours-title">Clinic Hours:</p>
      <p class="hours-note">(by appointment only)</p>
      <p class="hours-line">Monday to Thursday: 8:30am – 3:30pm</p>
      <p class="hours-line">Friday: 9:00am – 3:30pm</p>
      <p class="hours-line">Saturday &amp; Sunday: Close</p>
    </section>

    <section class="services-panel">
      We provide general skin care, surgical, pediatric, and laser surgery services for the treatment of diseases of the skin
    </section>
    <div class="footer-band"></div>
  </main>
</body>
</html>
```